Local Electrical company need some kick ass business cards

In need of some in your face design business cards for a family owned electrical service company in Edmonton, Alberta Canada. We provide reliable and trustworthy electrical service for commercial and residential work in the Edmonton and area. We have been in business for 25 years.

Target Market(s)

Residential and commercial electrical

Industry/Entity Type

Business

Contact Information for Business Card

Your welcome to change and modify the brightway electric logo. please include the lightbulb! Our Colours are black and green please stay with that.
Please include a name phone number and address on the card
phone number - 780-318-5062
#22, 418 Maple Cres, St.Albert, Alberta.
Two things that need to be on the card.
"your friendly neighborhood electrictrician"
Commercial & residential electrical repair and service

Colors
9bcb3c

Requirements
Must have
• Light bulb guy Attached
• "your friendly neighborhood electrictrician"
• Commercial & residential electrical repair and service
• phone number - 780-318-5062
• #22, 418 Maple Cres, St.Albert, Alberta.
• Our colours are black and green
Nice to have
• go wild i want something loud

```html
<!DOCTYPE html>
<html lang="en">
<head>
<meta charset="utf-8">
<title>Brightway Electric – Business Cards</title>
<link href="https://fonts.googleapis.com/css2?family=Open+Sans:wght@400;600;700;800&display=swap" rel="stylesheet">
<style>
  :root {
    --green: #8cc43f;
    --green-bright: #9bcb3c;
    --black: #111111;
    --white: #ffffff;
    --ink: #333333;
    --label: #f08a1c;
    --backdrop: #e9e9e6;
    --mascot-tone: #cfe3a8;
  }
  * { margin: 0; padding: 0; box-sizing: border-box; }
  html, body { width: 1200px; height: 1200px; overflow: hidden; }
  body {
    background: var(--backdrop);
    font-family: "Open Sans", Arial, sans-serif;
    position: relative;
  }
  .card {
    position: absolute;
    left: 150px;
    width: 900px;
    height: 514px;
    overflow: hidden;
    box-shadow: 0 6px 18px rgba(0,0,0,0.18);
  }
  /* Front: green side */
  .card-front { top: 64px; background: var(--green); }
  .mascot {
    position: absolute;
    left: 70px; top: 40px;
    width: 230px; height: 230px;
    border-radius: 16px;
    background: radial-gradient(circle at 50% 40%, #f4f7ee 0%, var(--mascot-tone) 60%, var(--green) 100%);
  }
  .tagline {
    position: absolute;
    left: 320px; top: 170px;
    color: var(--white);
    font-size: 24px;
    font-weight: 400;
  }
  .services {
    position: absolute;
    left: 0; right: 0; top: 330px;
    text-align: center;
    color: var(--white);
    font-size: 28px;
    font-weight: 600;
  }
  /* Back: white side */
  .card-back { top: 622px; background: var(--white); }
  .card-back svg.bands { position: absolute; inset: 0; }
  .person {
    position: absolute;
    left: 130px; top: 20px;
  }
  .person-name {
    color: var(--green);
    font-size: 30px;
    font-weight: 700;
    line-height: 1.15;
  }
  .person-role {
    color: var(--ink);
    font-size: 19px;
    font-weight: 600;
    line-height: 1.3;
  }
  .contact {
    position: absolute;
    left: 44px; top: 170px;
    color: var(--ink);
    font-size: 19px;
    line-height: 1.45;
    list-style: none;
  }
  .contact .gap { margin-bottom: 10px; }
  .contact .lbl { color: var(--label); font-weight: 600; }
  .brand {
    position: absolute;
    right: 60px; top: 210px;
    display: flex; align-items: center; gap: 14px;
  }
  .brand-dot {
    width: 40px; height: 40px; border-radius: 50%;
    background: var(--green);
  }
  .brand-name {
    color: var(--black);
    font-size: 34px;
    font-weight: 800;
    letter-spacing: 1px;
  }
</style>
</head>
<body>
  <section class="card card-front">
    <div class="mascot" role="img" aria-label="Cartoon light bulb mascot wearing a green cap"></div>
    <p class="tagline">your friendly neighborhood electrictrician</p>
    <p class="services">Commercial &amp; Residential Electrical Repair and Service</p>
  </section>

  <section class="card card-back">
    <svg class="bands" width="900" height="514" viewBox="0 0 900 514">
      <polygon points="40,22 80,22 54,62 40,62" fill="var(--black)"/>
      <polygon points="88,22 118,22 94,62 62,62" fill="var(--green)"/>
      <polygon points="0,400 350,400 330,440 0,440" fill="var(--black)"/>
      <polygon points="350,400 900,400 900,514 0,514 0,440 330,440" fill="var(--green)"/>
      <rect x="0" y="440" width="330" height="74" fill="var(--white)"/>
    </svg>
    <div class="person">
      <p class="person-name">Mark Dalton</p>
      <p class="person-role">Managing Director</p>
    </div>
    <ul class="contact">
      <li>#22, 418 Maple Cres,</li>
      <li class="gap">St.Albert, Alberta.</li>
      <li><span class="lbl">p:</span> 780-318-5062</li>
      <li><span class="lbl">f:</span> 780-318-5062</li>
      <li><span class="lbl">e:</span> info@brightwayelectric.ca</li>
    </ul>
    <div class="brand">
      <span class="brand-dot"></span>
      <span class="brand-name">BRIGHTWAY ELECTRIC</span>
    </div>
  </section>
</body>
</html>
```